Clean book cover design for book about writing a book

Book title: The Turning
Subtitle: 10 Paths to Crafting a Volume of Weight
Name: Mirela K. Dunwoody, The Quill Nestery

This is a book which teaches 10 steps to writing a self-help book. I'm looking for a very clean impactful cover either with no image or just a small simple image of a book, typewriter, laptop, cabin or something very simple. I am attaching the manuscript here if reading it would help you with the cover. The theme of the book is that you can write with joy and ease and your book can just flow out of you if you learn how to clear the blocks between you and your book already written. Sort of a new agey stance on book writing.

The book should generally match the branding on my website. Www.TheQuillNestery.example.

I have photos of myself attached which I'd like used for the back cover with an "about the author section of maybe 50 words.

The project is for the full back cover and spine as well as the front cover (see press Forge template attached) but to win the contest you can just design the front cover and then I'll give the winner the template for the full design with the back cover copy. Or you can design the full cover using the template and you can use Loren ipsum text if you need to.

My clients are very upmarket and the themes of my business revolve around nuturing and incubating ideas and authors. Very feminine creation energy.

For colors see The Turning Press (TH) wax seals and the background fades. I don't want my logo on the cover but I am attaching it here so you get a feel for the branding. The logo is in the LOBSTER font and you can see how we do the grey with the rainbow shadow.

Here are some covers I like:

http://www.bookmarto.example/Pen-Volume-Fast-Stage---Stage/dp/071302488Q
http://www.bookmarto.example/Sketching-Their-Tale-Chart-Triumph/dp/0865713511
http://www.bookmarto.example/Be-Scribe-Seeking-Poet-Guide-ebook/dp/C11G8V9PL7
http://www.bookmarto.example/Strayfolk-Tale-Triumph-Rupert-Hallowmere/dp/0427128041
Updates

I have revised my brief to include some picture and images that will help you create the cover. I have also included some of my favorite covers to give you more of a sense of what I'm going for. And I have included the manuscript in case it would help you to skim through it in order to get a sense of the reader and the book. I think if you look at my revised brief it will make it easier to create a submission. Thanks!

Target Market(s)

Women 40-60 who run small businesses as life coaches or other healing jobs (therapy, reiki, light work) they have a spiritual/new age bent.

Industry/Entity Type

Business

Font styles to use
Serif
Other font styles liked:
• Lobster (not required... just a suggestion since it's my logo font)

Requirements
Must have
• Name and title easy to read in 1" x 1" thumb nail
Nice to have
• Fantastic type face treatment.

Match the look and feel of my website.
Should not have
• Busy images. With one simple image or just designed with colors and typeface treatment

```html
<!DOCTYPE html>
<html lang="en">
<head>
<meta charset="utf-8">
<title>The Turning — Book Cover</title>
<link rel="stylesheet" href="https://fonts.googleapis.com/css2?family=Lato:wght@300;400;900&display=swap">
<style>
  :root {
    --page-bg: #e9eaeb;
    --paper: #ffffff;
    --title-teal: #19a6ad;
    --author-grey: #4a4d50;
    --band-teal: #28c4cf;
    --band-light: #52d0d6;
    --band-mist: #5fd4d9;
    --headline-ink: #2b5d73;
    --headline-glow: rgba(120, 225, 230, 0.9);
  }
  * { box-sizing: border-box; margin: 0; padding: 0; }
  html, body {
    width: 1200px;
    height: 900px;
    overflow: hidden;
    background: var(--page-bg);
  }
  .canvas {
    position: relative;
    width: 1200px;
    height: 900px;
  }
  .cover {
    position: absolute;
    left: 353px;
    top: 77px;
    width: 520px;
    height: 736px;
    background: var(--paper);
    overflow: hidden;
    font-family: "Lato", "Helvetica Neue", Arial, sans-serif;
  }
  .cover-band {
    position: absolute;
    inset: 0;
    width: 520px;
    height: 736px;
  }
  .cover-title {
    position: absolute;
    top: 38px;
    left: 0;
    width: 100%;
    text-align: center;
    font-weight: 900;
    font-size: 47px;
    letter-spacing: -0.5px;
    color: var(--title-teal);
    line-height: 1;
  }
  .cover-author {
    position: absolute;
    top: 97px;
    left: 0;
    width: 100%;
    text-align: center;
    font-weight: 400;
    font-size: 17px;
    color: var(--author-grey);
  }
  .cover-headline {
    position: absolute;
    left: 40px;
    top: 418px;
    color: var(--headline-ink);
    font-size: 66px;
    line-height: 60px;
    letter-spacing: -1.5px;
    text-transform: uppercase;
    text-shadow: 3px 3px 0 var(--headline-glow);
  }
  .cover-headline span { display: block; }
  .headline-strong { font-weight: 900; }
  .headline-light { font-weight: 300; }
</style>
</head>
<body>
  <main class="canvas">
    <article class="cover">
      <svg class="cover-band" viewBox="0 0 520 736" aria-hidden="true">
        <polygon points="0,355 520,268 520,736 0,736" fill="var(--band-teal)"/>
        <polygon points="0,628 520,268 520,736 0,736" fill="var(--band-light)"/>
        <polygon points="230,736 520,300 520,736" fill="var(--band-mist)"/>
      </svg>
      <h1 class="cover-title">THE TURNING</h1>
      <p class="cover-author">- Mirela K. Dunwoody -</p>
      <h2 class="cover-headline">
        <span class="headline-strong">10 Paths</span>
        <span class="headline-light">To Crafting</span>
        <span class="headline-strong">A Volume</span>
        <span class="headline-light">Of Weight</span>
      </h2>
    </article>
  </main>
</body>
</html>
```